Exciting new vermouth brand needs a brilliant label!

We need a label design for an exciting new premium Italian Vermouth brand called Lunavera Vermouth.

Lunavera Vermouth is based on a recipe that has been handed down for four generations and is made in the traditional way in the Piedmonte region of Northern Italy.

Lunavera, which means 'heavenly' in Italian has been designed to elevate classic cocktails such as the Negroni, Americano and Manhattan with a base of Italian wine blended with botanicals such as wormwood, orange peel, rhubarb and cinchona. It has a delicately balanced bittersweet profile with hints of vanilla and citrus.

Its competitors include brands such as Vecchia Ricetta, Brunetti and Fabrizzi (see the uploaded brief for more examples).

The label is for a 50cl dark bottle (please refer to the uploaded brief) and should be based on maximum dimensions of 70mm (width) x 110mm (height). There is no limit to embellishments such as foil printing, embossing or any other premium finishes. The label does not necessarily need to be rectangular.

Feedback will be given quickly and constructively after submissions to ensure that the process is as fair and useful as possible for everyone.

Target Market(s)

25-45 year old Europeans, 50:50 female:male

Industry/Entity Type

Wine / Spirits / Vermouth

Requirements
Must have
• Fantastic design that is distinct from competitors, a premium feel and great lettering.
Should not have
• Generic images or patterns that do not relate to the brand (Lunavera) or the product

```html
<!DOCTYPE html>
<html lang="en">
<head>
<meta charset="utf-8">
<title>Lunavera Vermouth – Label</title>
<link rel="stylesheet" href="https://fonts.googleapis.com/css2?family=Smokum&family=Libre+Baskerville:wght@700&family=Great+Vibes&display=swap">
<style>
  :root {
    --page: #ffffff;
    --shield-navy: #252446;
    --band-navy: #161a3a;
    --sky-deep: #0c2a78;
    --sky-teal: #0a8f93;
    --sky-green: #07a88a;
    --sky-night: #0b2350;
    --silver-light: #ffffff;
    --silver-mid: #d7d9dc;
    --silver-dark: #a9adb2;
    --rim-cyan: #5fd8f6;
    --rim-pink: #f3a7c4;
    --rim-peach: #f7dcc4;
    --ink-white: #ffffff;
  }
  html, body {
    margin: 0;
    padding: 0;
    width: 982px;
    height: 1200px;
    overflow: hidden;
    background: var(--page);
  }
  .label {
    display: block;
    width: 982px;
    height: 1200px;
  }
  .brand-title {
    font-family: "Smokum", "Rye", serif;
    font-size: 200px;
    fill: url(#silver);
  }
  .tagline {
    font-family: "Libre Baskerville", Georgia, serif;
    font-weight: 700;
    font-size: 44px;
    fill: var(--ink-white);
  }
  .origin {
    font-family: "Libre Baskerville", Georgia, serif;
    font-weight: 700;
    font-size: 33px;
    fill: var(--ink-white);
  }
  .origin-country {
    font-family: "Great Vibes", cursive;
    font-size: 115px;
    fill: var(--ink-white);
  }
</style>
</head>
<body>
<svg class="label" viewBox="0 0 982 1200" xmlns="http://www.w3.org/2000/svg">
  <defs>
    <linearGradient id="silver" x1="0" y1="0" x2="0" y2="1">
      <stop offset="0" stop-color="var(--silver-light)"/>
      <stop offset="0.5" stop-color="var(--silver-mid)"/>
      <stop offset="0.75" stop-color="var(--silver-light)"/>
      <stop offset="1" stop-color="var(--silver-dark)"/>
    </linearGradient>
    <linearGradient id="rim" x1="0" y1="0" x2="0.3" y2="1">
      <stop offset="0" stop-color="var(--rim-peach)"/>
      <stop offset="0.2" stop-color="var(--rim-cyan)"/>
      <stop offset="0.4" stop-color="var(--rim-pink)"/>
      <stop offset="0.6" stop-color="var(--rim-cyan)"/>
      <stop offset="0.8" stop-color="var(--rim-peach)"/>
      <stop offset="1" stop-color="var(--rim-cyan)"/>
    </linearGradient>
    <linearGradient id="sky" x1="0.2" y1="0" x2="0.5" y2="1">
      <stop offset="0" stop-color="var(--sky-deep)"/>
      <stop offset="0.3" stop-color="var(--sky-teal)"/>
      <stop offset="0.5" stop-color="#1d5f8e"/>
      <stop offset="0.7" stop-color="var(--sky-green)"/>
      <stop offset="1" stop-color="var(--sky-night)"/>
    </linearGradient>
    <radialGradient id="glow" cx="0.5" cy="0.38" r="0.45">
      <stop offset="0" stop-color="#6fd7d4" stop-opacity="0.55"/>
      <stop offset="1" stop-color="#6fd7d4" stop-opacity="0"/>
    </radialGradient>
    <clipPath id="panel-clip">
      <path d="M 500 55 Q 523 47 546 55 L 960 205 Q 988 215 987 245 L 947 1000 Q 945 1030 918 1045 L 550 1232 Q 523 1245 496 1232 L 128 1045 Q 101 1030 99 1000 L 59 245 Q 58 215 86 205 Z" transform="scale(0.9397 0.931)"/>
    </clipPath>
  </defs>

  <g class="shield" transform="scale(0.9397 0.931)">
    <path class="shield-outer" role="img" aria-label="Dark navy shield with faint flowing contour lines"
          fill="var(--shield-navy)"
          d="M 490 12 Q 523 0 556 12 L 985 150 Q 1025 165 1025 205 L 1025 1015 Q 1025 1058 988 1078 L 560 1275 Q 523 1290 486 1275 L 58 1078 Q 20 1058 20 1015 L 20 205 Q 20 165 60 150 Z"/>
  </g>

  <g class="sky-panel" clip-path="url(#panel-clip)" role="img" aria-label="Northern lights aurora glowing over a starry night sky">
    <rect width="982" height="1200" fill="url(#sky)"/>
    <rect width="982" height="1200" fill="url(#glow)"/>
  </g>

  <rect class="tagline-band" x="90" y="664" width="802" height="88" fill="var(--band-navy)" clip-path="url(#panel-clip)"/>

  <path class="panel-rim" fill="none" stroke="url(#rim)" stroke-width="5" vector-effect="non-scaling-stroke"
        transform="scale(0.9397 0.931)"
        d="M 500 55 Q 523 47 546 55 L 960 205 Q 988 215 987 245 L 947 1000 Q 945 1030 918 1045 L 550 1232 Q 523 1245 496 1232 L 128 1045 Q 101 1030 99 1000 L 59 245 Q 58 215 86 205 Z"/>

  <text class="brand-title" x="131" y="428" textLength="705" lengthAdjust="spacingAndGlyphs">LUNAVERA</text>
  <text class="brand-title" x="180" y="610" textLength="630" lengthAdjust="spacingAndGlyphs">VERMOUTH</text>

  <text class="tagline" x="211" y="726" textLength="577" lengthAdjust="spacingAndGlyphs">ELEVATE YOUR COCKTAILS</text>

  <text class="origin" x="305" y="870" textLength="370" lengthAdjust="spacingAndGlyphs">MADE IN PIEDMONT,</text>
  <text class="origin-country" x="482" y="1010" text-anchor="middle">Italy</text>
</svg>
</body>
</html>
```